Store Front Window Design

We have a beautiful corner store front dental practice with no window signage. Crazy I know...that's why we need your help.

The final design will be done in all vinyl unless unless you suggest a different medium (meaning we are open to some design idea like using frosted glass, etc...).

The windows provide a lot of natural light so the design needs to keep a lot of natural light coming into the office. Keep in mind vinyl is not opaque so keep the signage aesthetically pleasing and a minimalist design to allow as much natural light in as possible. The design should follow the aesthetic from our logo. or tie into at least. We want a cohesive brand aesthetic.

I submitted some general layout ideas. There is a blue banner with advertising words which we want to be used in the final version. Even though the lettering is black, in reality the letters will be a white vinyl on the outside of the window. When you submit your work, be sure to add any special instructions (aka tell me the vision for the letters is white not black, maybe gold leaf, or forested glass...stuff like that). AND YOU DO NOT HAVE TO FOLLOW MY PATTERN! YOU ARE ARTISTS AND WE ARE LOOKING FOR AN ARTISTIC EYE CATCHING PRESENTATION OF THIS INFORMATION. MAKE IT FLASHY AND ADD SOME AESTHETIC FROM THE TOOTH LOGO.

The store front is 6 windows roughly 60'' x 36'' The smaller windows below are 27'' x 36''. Around the corner there are 3 windows. they are 60'' x 27'' lower windows are 27" x 27". We would like to keep the bottom windows clear and keep the signage on the top windows, however, we are flexible.

The front 6 windows need to have this information worked into the design.

Practice name: Vesk and Ormond Dental & Orthodontics.
Phone numbers: Marisol Vesk DDS: 415.772.0183
Tobias Ormond DDS:415.509.2371

Expertise: Dr. Vesk General Dentistry & Orthodontics
Dr. Ormond Oral Surgery & Sedation

Address: 1937 Birchwood Ave

A banner across the bottom of the top windows with some key advertisement words: "Clarivet" "Braces" "Implants" "Whiting" "Call today" "Free Consultation" "Oral Surgery" "Sedation". We like the two color idea. Its up to you to decide on the color combo. I used a Dark and light blue, but maybe a Blue and grey would nice to tire in the logo colors?

I have made some mock ideas to get the ball rolling but you do not have to stick to these designs at all, just as long as all the required information is there. Be creative with the layouts, fonts, color scheme, (just remember these are going on windows not necessarily a white background), and graphics/artistic flare (refer to logo for layout inspiration and use the logo as an actual graphic). We are running a miltimillion dollar dental practice so we want these windows to be eye catching to pull in patients and look like a million dollar design. Also all 6 windows dont need ot be used. I am really looking for creative design marketing.

The corner 3 windows need the following information: name, expertise, phone number, banner.

Dr. Vesk, General Dentistry & Orthodontics, 415.772.0183
Dr. Ormond, Oral Surgery & Sedation, 415.509.2371

There is also a front door that needs to be designed. The door is 60'' x 36'' (standard door size) We want simple white vinyl on the outside of the door. We need you to organize the information on the door, pick a easy to read font, maybe use the logo and use some of the front window signage aesthetic? Its up to you...but we we were initially thinking of just making the litters white and keep it simple but again you are the designers.

Practice name: Vesk and Ormond General Dentistry & Orthodontics

Address: 1937 Birchwood Ave

Phone numbers: Dr. Vesk 415.772.0183
Dr. Ormond 415.509.2371

Hours of operation: Mon: call for an appointment
Tues-Thurs: 9am-5pm
Sat: call for an appointment
Sun: Closed

A line saying we speak Spanish: Se Habla Espanol

*****************************************************************************************************
here are some design that we liked and some rough sketches I made to start the ball rolling. Keep in mind that there are 9 windows for the front because its a corner office, but not all of them have to have stuff on it. We want simple, streamline, classy high commanding price point aesthetic. I am hiring you for your artistic minds.

Target Market(s)

anyone who has dental needs

Industry/Entity Type

Dental

Font styles to use
Serif
Sans Serif

Colors

Designer to choose colors to be used in the design.

Requirements
Must have
• 1. The required information (see project description)
• 2. Logo
• 3. Advertisement banner running along the bottom of all 9 windows (6 in front and 3 on the side)
• NOTE: Look at pictures of the store to get a sense of the customers point of view and also as a reference to how your design will be broken up across several windows or maybe you design something special for every window. But we want the banner to run along all the windows to lead customs to the door on the side. Finally the letters will be done in white vinyl unless state otherwise, remember the window needs to let in natural light so the entire window can not be covered in vinyl.
Nice to have
• artistic flare yet simple and sleep and expensive looking aesthetic. work logo into the design.
Should not have
• The goal is to catch someone eye and give them important information about the practice.
• It should not just be words.
• It should not have to many words
• It must be readable font for cards driving by.

```html
<!DOCTYPE html>
<html lang="en">
<head>
<meta charset="utf-8">
<title>Vesk and Ormond — Front Door Sign</title>
<link href="https://fonts.googleapis.com/css2?family=Oswald:wght@400;500&family=Varela+Round&family=Great+Vibes&family=Montserrat:wght@500;600;700&display=swap" rel="stylesheet">
<style>
  :root {
    --bg: #e4e4e4;
    --sign: #ffffff;
    --blue: #1476c8;
    --blue-deep: #0d5fa8;
    --grey: #6b6b6d;
    --grey-line: #9a9a9a;
    --ink: #1a1a1a;
  }
  html, body { margin: 0; padding: 0; overflow: hidden; }
  body { width: 1200px; height: 960px; background: var(--bg); position: relative; }

  .door-sign {
    position: absolute; left: 354px; top: 40px;
    width: 493px; height: 820px;
    background: var(--sign);
    box-shadow: 0 6px 12px rgba(0,0,0,.25);
    overflow: hidden;
  }
  .corner-swoosh { position: absolute; right: 0; top: 0; }

  .practice-name { position: absolute; left: 0; width: 100%; top: 150px; margin: 0; text-align: center;
    font-family: "Montserrat", sans-serif; font-weight: 600; color: var(--grey); line-height: 1.2; }
  .practice-name .partners { display: block; font-size: 15px; letter-spacing: 6px; margin-bottom: 1px; color: var(--blue-deep); }
  .practice-name .specialty { display: block; font-size: 21px; }

  .street-number { position: absolute; left: 0; width: 100%; top: 212px; text-align: center;
    font-family: "Oswald", sans-serif; font-weight: 500; font-size: 74px; line-height: 74px; color: var(--blue); }
  .street-band { position: absolute; left: 0; width: 100%; top: 293px; height: 39px; background: var(--blue);
    color: #fff; text-align: center; font-family: "Montserrat", sans-serif; font-weight: 500;
    font-size: 28px; line-height: 40px; }

  .hours-box { position: absolute; left: 85px; top: 378px; width: 320px; height: 180px;
    border: 1px solid var(--grey-line); box-sizing: border-box; }
  .hours-title { position: absolute; left: 99px; top: 367px; width: 296px; height: 44px;
    background: var(--grey); color: #fff; text-align: center; font-family: "Oswald", sans-serif;
    font-size: 34px; line-height: 44px; }
  .hours-list { position: absolute; left: 85px; width: 320px; top: 420px; margin: 0; padding: 0;
    list-style: none; text-align: center; font-family: "Varela Round", sans-serif; font-size: 19px;
    color: var(--blue); line-height: 31px; }

  .doctor { position: absolute; top: 595px; width: 240px; text-align: center; }
  .doctor--vesk { left: 8px; }
  .doctor--ormond { left: 244px; }
  .doctor-name { font-family: "Oswald", sans-serif; font-size: 31px; color: var(--blue); line-height: 34px; }
  .doctor-field { font-family: "Varela Round", sans-serif; font-size: 14.5px; color: var(--grey);
    line-height: 18px; margin-top: 8px; }
  .doctor-phone { font-family: "Oswald", sans-serif; font-size: 32px; color: var(--blue); line-height: 44px; margin-top: 4px; }

  .footer-rule { position: absolute; left: 0; width: 100%; top: 757px; height: 5px; background: var(--blue); }
  .spanish-line { position: absolute; left: 0; width: 100%; top: 766px; text-align: center;
    font-family: "Great Vibes", cursive; font-size: 38px; line-height: 48px; color: var(--ink); }

  .piece-label { position: absolute; left: 0; width: 100%; top: 880px; text-align: center;
    font-family: "Montserrat", sans-serif; font-weight: 700; font-size: 32px; color: var(--ink); letter-spacing: 1px; }
</style>
</head>
<body>
  <section class="door-sign">
    <svg class="corner-swoosh" width="260" height="190" viewBox="0 0 260 190" aria-hidden="true">
      <path d="M0 0 H260 V180 C220 90 130 20 0 0 Z" fill="var(--blue)"/>
      <path d="M0 0 C130 20 220 90 260 180 V190 C215 100 125 25 0 0 Z" fill="var(--blue-deep)"/>
    </svg>

    <h1 class="practice-name">
      <span class="partners">VESK AND ORMOND</span>
      <span class="specialty">DENTAL &amp; ORTHODONTICS</span>
    </h1>

    <div class="street-number">1937</div>
    <div class="street-band">BIRCHWOOD AVENUE</div>

    <div class="hours-box"></div>
    <div class="hours-title">HOURS OF OPERATION</div>
    <ul class="hours-list">
      <li>Mon : Call for an appointment</li>
      <li>Tues - Thurs : 9am-5pm</li>
      <li>Sat : Call for an appointment</li>
      <li>Sun : Closed</li>
    </ul>

    <div class="doctor doctor--vesk">
      <div class="doctor-name">DR. VESK</div>
      <div class="doctor-field">General Dentistry<br>&amp;<br>Orthodontics</div>
      <div class="doctor-phone">415.772.0183</div>
    </div>
    <div class="doctor doctor--ormond">
      <div class="doctor-name">DR. ORMOND</div>
      <div class="doctor-field">Oral Surgery<br>&amp;<br>Sedation Dentistry</div>
      <div class="doctor-phone">415.509.2371</div>
    </div>

    <div class="footer-rule"></div>
    <div class="spanish-line">Se Habla Espanol</div>
  </section>

  <div class="piece-label">FRONT DOOR</div>
</body>
</html>
```